Flyer Project for Industrial Company

We need to change an old flyer and update with new information. Could have some updated design elements! Like the second page design. Keep the text the same. I have added some photos that we would like to use and have more.
We would like it to be professional, it is going out in a direct mail so we need it to be eye catching.
Target Market(s)
General Contracors
Industry/Entity Type
industrial services
Font styles to use
Serif
Sans Serif
Colors
EB3D1F
EC4F4E
F09395
F8D3D4
FCEDEE
Requirements
Must have
- Updated design and modern elements

```html
<!DOCTYPE html>
<html lang="en">
<head>
<meta charset="utf-8">
<title>R.K. Halden Companies – Flyer</title>
<link rel="stylesheet" href="https://fonts.googleapis.com/css2?family=Arimo:wght@400;700&family=Fira+Sans+Condensed:wght@700&family=Libre+Baskerville:wght@700&display=swap">
<style>
  :root {
    --red: #e3212f;
    --ink: #1a1a1a;
    --band: #5a5a5a;
    --band-dark: #4a4a4a;
    --white: #ffffff;
  }
  html, body { margin: 0; padding: 0; overflow: hidden; background: #fff; }
  .flyer {
    position: relative; width: 927px; height: 1200px; overflow: hidden;
    background: var(--white); font-family: "Arimo", Arial, sans-serif; color: var(--ink);
  }
  .hero-photo {
    position: absolute; left: 0; top: 0; width: 641px; height: 567px;
    background: linear-gradient(180deg, #6f9acb 0%, #a9c3e0 30%, #8a8f8c 52%, #6b5a48 70%, #4a3e35 100%);
  }
  .title-band {
    position: absolute; left: 0; top: 492px; width: 535px; height: 75px;
    background: rgba(85, 85, 85, 0.92);
  }
  .title-band h1 {
    margin: 0; position: absolute; left: 23px; top: 11px;
    font-family: "Libre Baskerville", "Times New Roman", serif; font-weight: 700;
    font-size: 39.5px; color: var(--white); letter-spacing: -0.5px; white-space: nowrap;
  }
  .collage { position: absolute; left: 640px; top: 0; width: 287px; height: 610px; }
  .section-title {
    position: absolute; left: 43px; top: 582px; margin: 0;
    font-family: "Fira Sans Condensed", "Arial Narrow", sans-serif; font-weight: 700;
    font-size: 34.5px; color: var(--red);
  }
  .intro {
    position: absolute; left: 39px; top: 630px; width: 858px; margin: 0;
    font-size: 17px; line-height: 21.7px;
  }
  .invite { position: absolute; left: 39px; top: 764px; margin: 0; font-size: 17px; white-space: nowrap; }
  .list-title {
    position: absolute; top: 832px; margin: 0; font-weight: 400;
    font-size: 24px; color: var(--red);
  }
  .list-title.services { left: 43px; }
  .list-title.expertise { left: 473px; }
  .list { position: absolute; margin: 0; padding: 0; list-style: none; font-size: 18px; }
  .list li { position: relative; height: 27.2px; line-height: 27.2px; white-space: nowrap; }
  .list li::before {
    content: ">"; position: absolute; color: var(--red); font-size: 18px;
  }
  .services-list { left: 94px; top: 887px; }
  .services-list li::before { left: -24px; }
  .expertise-list { left: 533px; top: 899px; }
  .expertise-list li::before { left: -28px; }
  .footer-band {
    position: absolute; left: 0; top: 1124px; width: 927px; height: 76px;
    background: linear-gradient(90deg, var(--band) 0%, #666 50%, var(--band-dark) 100%);
  }
  .tagline {
    position: absolute; left: 85px; top: 19px; margin: 0;
    font-size: 30px; color: var(--white); white-space: nowrap;
  }
  .brand {
    position: absolute; left: 690px; top: 21px; display: flex; align-items: center; gap: 8px;
  }
  .brand-square { width: 28px; height: 28px; background: var(--red); }
  .brand-name {
    font-family: "Arimo", Arial, sans-serif; font-weight: 700; font-size: 16px;
    color: var(--white); line-height: 18px;
  }
</style>
</head>
<body>
<div class="flyer">
  <div class="hero-photo" role="img" aria-label="Photo of a demolition site with piles of twisted steel debris, an excavator and crew in front of a stadium under a blue cloudy sky"></div>
  <div class="title-band"><h1>R.K. Halden Companies</h1></div>

  <svg class="collage" viewBox="640 0 287 610" width="287" height="610">
    <defs>
      <linearGradient id="sky" x1="0" y1="0" x2="0" y2="1"><stop offset="0" stop-color="#7fa6d2"/><stop offset="1" stop-color="#c9d6e3"/></linearGradient>
      <linearGradient id="fire" x1="0" y1="0" x2="0" y2="1"><stop offset="0" stop-color="#d9dadb"/><stop offset="0.6" stop-color="#8a8a86"/><stop offset="1" stop-color="#55524d"/></linearGradient>
      <linearGradient id="silo" x1="0" y1="0" x2="0" y2="1"><stop offset="0" stop-color="#9fc0e2"/><stop offset="0.5" stop-color="#6f7b86"/><stop offset="1" stop-color="#8a7d6a"/></linearGradient>
      <linearGradient id="plant" x1="0" y1="0" x2="0" y2="1"><stop offset="0" stop-color="#d7dee6"/><stop offset="0.5" stop-color="#c2403a"/><stop offset="1" stop-color="#8e8270"/></linearGradient>
      <linearGradient id="scrap" x1="0" y1="0" x2="1" y2="1"><stop offset="0" stop-color="#6b6660"/><stop offset="1" stop-color="#4a3f36"/></linearGradient>
    </defs>
    <polygon points="674,0 927,0 927,148" fill="url(#sky)" role="img" aria-label="Photo fragment of sky over a demolished building"/>
    <polygon points="660,15 895,151 660,287" fill="url(#fire)" role="img" aria-label="Photo of firefighters and a ladder truck at a smoking demolition site"/>
    <polygon points="654,309 907,166 907,457" fill="url(#silo)" role="img" aria-label="Photo of steel silos being dismantled by an excavator"/>
    <polygon points="660,337 895,470 660,609" fill="url(#plant)" role="img" aria-label="Photo of an excavator demolishing a red industrial building"/>
    <polygon points="766,567 927,473 927,567" fill="url(#scrap)" role="img" aria-label="Photo fragment of scrap metal debris"/>
  </svg>

  <h2 class="section-title">The Industry Leader</h2>
  <p class="intro">The R. K. Halden Family has been committed to excellence for over 60 years, growing to a network of more than 1,000 employees with offices in 10 states. We offer demolition, environmental, infrastructure, rigging and equipment installation services to both the public and private sector. Combining our experienced employee base with our financial strength, bonding capacity and equipment resources, RKH provides efficient and cost effective turnkey services.</p>
  <p class="invite">We welcome our future clients and invite you to see what the R.K. Halden Companies can do for you.</p>

  <h3 class="list-title services">Our Services Include:</h3>
  <h3 class="list-title expertise">Our Areas of Expertise:</h3>

  <ul class="list services-list">
    <li>Emergency Response</li>
    <li>Conventional and Explosive Demolition</li>
    <li>Environmental Services</li>
    <li>Grading, Excavation and infrastructure</li>
    <li>Asbestos Abatement</li>
    <li>Rigging, Machinery Moving, Equipment Install</li>
  </ul>

  <ul class="list expertise-list">
    <li>Industrial</li>
    <li>Commercial</li>
    <li>Turn-key projects</li>
  </ul>

  <footer class="footer-band">
    <p class="tagline">Shaping America’s Skyline since 1959.</p>
    <div class="brand">
      <span class="brand-square"></span>
      <span class="brand-name">R.K. HALDEN<br>Companies</span>
    </div>
  </footer>
</div>
</body>
</html>
```